Letterhead Design Project (logo provided)

We are a legal services provider company called VRN Legal based in the UK and would like some letterhead paper designed.

The design should use the attached logo, and should use the colors feature in the logo (along with blacks and/or greys).

The background paper must be white - and A4 size.

The letterhead should be provided in both .pdf and .doc (or .odf) formats.

Target Market(s)

Customers and clients for legal services

Industry/Entity Type

Legal

Requirements
Must have
• The header must include the following information:

Business name - VRN Legal LLP
Office address - Larchmead Court, Wallingford, Oxfordshire OX10 4TL, United Kingdom
Telephone - +44 (0)1491 736480
Email - mail@ [domain given below]
Website: www.vrnlegal-example.com

The footer must include the following information:

Registered office address - 14 Alder Row, Brindlecote, Wallingford, Oxfordshire OX10 6QD, United Kingdom
Companies House registration number - OC718463
VAT registration number - GB 417386205

```html
<!DOCTYPE html>
<html lang="en">
<head>
<meta charset="utf-8">
<title>VRN Legal LLP – Letterhead</title>
<link rel="stylesheet" href="https://fonts.googleapis.com/css2?family=Tinos:wght@400;700&display=swap">
<style>
  :root {
    --paper: #ffffff;
    --ink-blue: #0b4ea2;
    --brand-blue: #1c3f94;
    --brand-green: #2e9e3a;
  }
  html, body {
    margin: 0;
    padding: 0;
    overflow: hidden;
    background: var(--paper);
  }
  .letterhead {
    position: relative;
    width: 927px;
    height: 1200px;
    background: var(--paper);
    font-family: "Tinos", "Times New Roman", serif;
    color: var(--ink-blue);
    overflow: hidden;
  }
  .brand {
    position: absolute;
    left: 34px;
    top: 70px;
    display: flex;
    align-items: center;
    gap: 14px;
  }
  .brand-dot {
    width: 30px;
    height: 30px;
    border-radius: 50%;
    background: var(--brand-green);
  }
  .brand-name {
    font-size: 50px;
    font-weight: 700;
    color: var(--brand-blue);
    line-height: 1;
    letter-spacing: 0.5px;
  }
  .contact {
    position: absolute;
    left: 571px;
    top: 62px;
    margin: 0;
    font-size: 18.6px;
    line-height: 21.8px;
    font-style: normal;
  }
  .contact p { margin: 0; white-space: nowrap; }
  .footer {
    position: absolute;
    left: 0;
    right: 0;
    top: 1118px;
    text-align: center;
    font-size: 18.4px;
    line-height: 22px;
  }
  .footer p { margin: 0; white-space: nowrap; }
</style>
</head>
<body>
  <div class="letterhead">
    <header>
      <div class="brand">
        <span class="brand-dot" aria-hidden="true"></span>
        <span class="brand-name">VRN Legal</span>
      </div>
      <address class="contact">
        <p>Office address - Larchmead Court, Wallingford,</p>
        <p>Oxfordshire OX10 4TL, United Kingdom</p>
        <p>Telephone - +44 (0)1491 736480</p>
        <p>Email - mail@ [domain given below]</p>
        <p>Website: www.vrnlegal-example.com</p>
      </address>
    </header>
    <footer class="footer">
      <p>Registered office address - 14 Alder Row, Brindlecote, Wallingford, Oxfordshire OX10 6QD, United Kingdom</p>
      <p>Companies House registration number - OC718463 VAT registration number - GB 417386205</p>
    </footer>
  </div>
</body>
</html>
```